Brixo Tidy Yard Website

We need a website design for this new company. I've attached the company logo. This company is in the construction industry that provides general labor, maintenance and cleaning for construction sites. We want a clean and simple website that can be easy to navigate.

Target Market(s)

Construction industry

Industry/Entity Type

Construction

Number of Pages Required

2 page

Font styles to use
Sans Serif

```html
<!DOCTYPE html>
<html lang="en">
<head>
<meta charset="utf-8">
<title>Brixo Tidy Yard</title>
<link rel="stylesheet" href="https://fonts.googleapis.com/css2?family=Poppins:wght@400;500;600;700&family=Open+Sans:wght@400;600&display=swap">
<style>
:root{
  --green:#34a35a;
  --green-dark:#2a8a4a;
  --yellow:#f2c21b;
  --orange:#f47b20;
  --ink:#222;
  --dark:#2b2b2b;
  --darker:#1e1e1e;
  --text:#6f6f6f;
  --muted:#9a9a9a;
  --line:#e4e4e4;
  --light:#f4f4f4;
  --white:#fff;
}
*{box-sizing:border-box;margin:0;padding:0}
html,body{width:1200px;height:3346px;overflow:hidden}
body{font-family:"Open Sans",Arial,sans-serif;color:var(--text);background:var(--white);position:relative;font-size:12px;line-height:1.6}
h1,h2,h3,h4{font-family:"Poppins",Arial,sans-serif;color:var(--ink)}
.abs{position:absolute}
.photo{position:absolute}

/* top bar */
.topbar{position:absolute;left:0;top:0;width:1200px;height:27px;background:var(--darker);color:#bbb;font-size:10px}
.topbar .contact{position:absolute;left:256px;top:6px;display:flex;gap:22px}
.topbar .social{position:absolute;right:252px;top:8px;display:flex;gap:14px}
.dot{width:10px;height:10px;border-radius:50%;background:#bbb;display:block}

/* hero */
.hero{position:absolute;left:0;top:27px;width:1200px;height:393px;background:linear-gradient(110deg,#3d3f3d 0%,#6c6a62 35%,#c7732d 55%,#8a8173 75%,#4b4c4a 100%)}
.hero-title{position:absolute;left:228px;top:160px;width:300px;font-family:"Poppins",sans-serif;font-weight:600;font-size:24px;line-height:1.3;color:var(--white)}
.hero-sub{position:absolute;left:228px;top:232px;width:250px;font-size:12px;color:#eee}
.hero-arrow{position:absolute;top:244px;width:22px;height:30px;background:rgba(0,0,0,.45);display:flex;align-items:center;justify-content:center}

/* nav */
.nav{position:absolute;left:234px;top:27px;width:732px;height:73px;background:var(--white);display:flex;align-items:center}
.brand{margin-left:28px;display:flex;align-items:center;gap:8px;font-family:"Poppins",sans-serif;font-weight:700;font-size:15px;color:var(--ink)}
.brand i{width:14px;height:14px;background:var(--orange);display:block}
.menu{margin-left:auto;margin-right:22px;display:flex;gap:34px;font-family:"Poppins",sans-serif;font-size:10px;font-weight:500;color:#444}
.menu .active{color:var(--green)}
.strip{position:absolute;left:234px;top:100px;width:732px;height:43px;background:var(--green);display:flex;color:var(--white);font-size:8px;line-height:1.35}
.strip-item{display:flex;align-items:center;gap:8px;width:120px;margin-left:28px}
.strip-item b{font-family:"Poppins",sans-serif;font-weight:600}
.tick{width:18px;height:18px;flex:none}
.strip-cta{margin-left:auto;display:flex;align-items:center;background:var(--green-dark);padding:0 14px;gap:22px;font-family:"Poppins",sans-serif;font-weight:600;font-size:8px}
.strip-cta .dl{background:var(--yellow);color:var(--ink);padding:15px 14px}

/* stats */
.stats{position:absolute;left:0;top:420px;width:1200px;height:108px;background:var(--dark)}
.stat{position:absolute;top:28px;color:#ddd;font-family:"Poppins",sans-serif;font-size:9px;font-weight:500;text-transform:uppercase}
.stat strong{display:block;font-size:30px;line-height:1;color:var(--green);font-weight:600;margin-bottom:6px}
.talk{position:absolute;left:787px;top:420px;width:188px;height:108px;background:var(--darker);color:var(--white);font-family:"Poppins",sans-serif;font-size:13px;font-weight:500;padding:34px 22px;line-height:1.5}

/* who */
.eyebrow{font-family:"Poppins",sans-serif;font-size:8px;color:var(--muted);text-transform:uppercase;letter-spacing:.5px}
.title{font-family:"Poppins",sans-serif;font-weight:600;font-size:15px;color:var(--ink);text-transform:uppercase}
.who-head{position:absolute;left:220px;top:553px}
.who-text{position:absolute;left:220px;top:612px;width:440px;font-size:10.5px}
.quote{position:absolute;left:220px;top:682px;width:500px;padding-left:32px;font-size:13px;color:#999;line-height:1.65}
.quote::before{content:"\201C";position:absolute;left:0;top:-10px;font-size:46px;color:#ccc;font-family:Georgia,serif}

/* bands */
.band{position:absolute;top:836px;height:127px;width:400px;color:var(--white);text-align:center;padding-top:46px;font-size:10px}
.band b{display:block;font-family:"Poppins",sans-serif;font-size:10px;text-transform:uppercase;font-weight:600}

/* services */
.ind-head{position:absolute;left:234px;top:996px}
.ind-text{position:absolute;left:234px;top:1060px;width:360px;font-size:10px}
.tabs{position:absolute;left:234px;top:1135px;width:230px;border-right:1px solid var(--line)}
.tab{height:45px;border-bottom:1px solid var(--line);padding-left:32px;line-height:45px;font-family:"Poppins",sans-serif;font-size:8.5px;font-weight:500;color:#444;text-transform:uppercase}
.tab.active{color:var(--green);border-left:2px solid var(--green);background:#fafafa;border-top:1px solid var(--line)}
.ind-caption{position:absolute;left:484px;top:1366px;width:482px}
.ind-caption h4{font-size:12px;font-weight:600;margin-bottom:6px}
.ind-caption p{font-size:10px}

/* projects */
.projects{position:absolute;left:0;top:1490px;width:1200px;height:481px;background:var(--dark);text-align:center}
.projects .eyebrow{position:absolute;top:34px;width:100%}
.projects .title{position:absolute;top:48px;width:100%;color:var(--white)}
.filters{position:absolute;left:410px;top:104px;width:380px;height:26px;background:var(--darker);display:flex;justify-content:space-around;align-items:center;font-family:"Poppins",sans-serif;font-size:7.5px;color:#bbb;text-transform:uppercase}
.filters .on{color:var(--white);border-bottom:2px solid var(--orange);padding-bottom:3px}

/* features */
.feat-head{position:absolute;left:234px;top:2010px}
.feature{position:absolute;width:230px;display:flex;gap:14px}
.feature .ico{width:36px;height:36px;background:#eef3ef;flex:none;display:flex;align-items:center;justify-content:center}
.feature h4{font-size:8.5px;font-weight:600;text-transform:uppercase;margin:2px 0 5px}
.feature p{font-size:8.5px;line-height:1.6}
.testi{position:absolute;left:722px;top:2007px;width:253px;height:297px;background:var(--light);padding:28px 28px}
.testi .qmark{position:absolute;left:28px;top:36px;width:22px;height:22px;background:var(--yellow)}
.testi .avatar{position:absolute;left:58px;top:30px;width:42px;height:34px;background:linear-gradient(#c9c2b6,#7b7a74)}
.testi h4{position:absolute;left:28px;top:84px;font-size:12px;font-weight:600}
.testi .role{position:absolute;left:28px;top:102px;font-size:8px;color:var(--muted)}
.testi p{position:absolute;left:28px;top:128px;width:200px;font-size:11px;line-height:1.75;color:#888}

/* news */
.news-head{position:absolute;top:2337px;width:1200px;text-align:center}
.card{position:absolute;top:2420px;width:232px}
.card .meta{margin-top:22px;font-size:7.5px;color:var(--muted)}
.card .meta b{color:var(--green);font-weight:600}
.card h4{font-size:11.5px;font-weight:600;line-height:1.45;margin:6px 0 8px}
.card p{font-size:8.5px;line-height:1.6}

/* partners */
.partners{position:absolute;left:262px;top:2772px;width:700px;display:flex;justify-content:space-between;align-items:center}
.partner{width:58px;height:28px;background:#d4d4d4}
.partner.round{width:30px;border-radius:50%}

/* contact */
.contact-sec{position:absolute;left:0;top:2859px;width:1200px;height:410px;background:var(--light)}
.contact-head{position:absolute;left:234px;top:2907px}
.contact-brand{position:absolute;left:408px;top:2918px;display:flex;align-items:center;gap:6px;font-family:"Poppins",sans-serif;font-weight:700;font-size:12px;color:var(--ink)}
.contact-brand i{width:10px;height:10px;background:var(--orange);display:block}
.contact-text{position:absolute;left:234px;top:2968px;width:340px;font-size:10.5px}
.info{position:absolute;top:3058px;width:120px;border-top:1px solid var(--line);padding-top:16px}
.info .lbl{font-size:7px;color:var(--muted);text-transform:uppercase;margin:8px 0 4px}
.info .val{font-family:"Poppins",sans-serif;font-size:10px;font-weight:600;color:var(--ink);line-height:1.5}
.form{position:absolute;left:598px;top:2906px;width:368px;height:316px;background:var(--white);padding:38px 26px}
.form h3{text-align:center;font-size:15px;font-weight:600;text-transform:uppercase;margin-bottom:20px}
.row{display:flex;gap:12px;margin-bottom:12px}
.field{flex:1;height:28px;border:1px solid var(--line);font-size:8px;color:#aaa;padding:8px 10px}
.field.area{height:60px}
.btn{height:28px;background:var(--orange);color:var(--white);text-align:center;line-height:28px;font-family:"Poppins",sans-serif;font-weight:600;font-size:8.5px;text-transform:uppercase}

/* footer */
.footer{position:absolute;left:0;top:3269px;width:1200px;height:77px;background:var(--darker);font-size:8px;color:#888}
.footer .top{position:absolute;left:572px;top:36px;text-transform:uppercase}
.footer .copy{position:absolute;right:244px;top:31px}
.footer .notch{position:absolute;left:590px;top:0;width:0;height:0;border-left:10px solid transparent;border-right:10px solid transparent;border-top:10px solid var(--light)}
</style>
</head>
<body>

<header>
  <div class="topbar">
    <div class="contact"><span>1800 - 555 204 19</span><span>office@brixotidy.com</span></div>
    <div class="social"><i class="dot"></i><i class="dot"></i><i class="dot"></i><i class="dot"></i><i class="dot"></i></div>
  </div>

  <section class="hero" role="img" aria-label="Photo of site workers in orange safety gear and hard hats reviewing plans on a construction site">
    <h1 class="hero-title">Leader in site labour and cleanup</h1>
    <p class="hero-sub">Safe, tidy and ready sites with crews you can trust every day.</p>
    <span class="hero-arrow" style="left:12px"><svg width="8" height="12" viewBox="0 0 8 12"><path d="M6 1 1 6l5 5" stroke="#fff" fill="none" stroke-width="1.6"/></svg></span>
    <span class="hero-arrow" style="right:12px"><svg width="8" height="12" viewBox="0 0 8 12"><path d="m2 1 5 5-5 5" stroke="#fff" fill="none" stroke-width="1.6"/></svg></span>
  </section>

  <nav class="nav">
    <div class="brand"><i></i>Brixo Tidy Yard</div>
    <div class="menu">
      <span class="active">HOME ⌄</span><span>SERVICES ⌄</span><span>PROJECT ⌄</span><span>NEW ⌄</span><span>PAGE ⌄</span><span>THEME ⌄</span>
      <svg width="11" height="11" viewBox="0 0 11 11"><circle cx="4.5" cy="4.5" r="3.5" stroke="#333" fill="none" stroke-width="1.3"/><path d="m7 7 3 3" stroke="#333" stroke-width="1.3"/></svg>
    </div>
  </nav>
  <div class="strip">
    <div class="strip-item"><svg class="tick" viewBox="0 0 18 18"><circle cx="9" cy="9" r="8" fill="none" stroke="#fff"/><path d="m5 9 3 3 5-6" fill="none" stroke="#fff" stroke-width="1.5"/></svg><span><b>Site Crews</b><br>Ready at short notice</span></div>
    <div class="strip-item"><svg class="tick" viewBox="0 0 18 18"><circle cx="9" cy="9" r="8" fill="none" stroke="#fff"/><path d="m5 9 3 3 5-6" fill="none" stroke="#fff" stroke-width="1.5"/></svg><span><b>Certified</b><br>Safety trained staff</span></div>
    <div class="strip-item"><svg class="tick" viewBox="0 0 18 18"><circle cx="9" cy="9" r="8" fill="none" stroke="#fff"/><path d="m5 9 3 3 5-6" fill="none" stroke="#fff" stroke-width="1.5"/></svg><span><b>Number #1</b><br>In site cleaning</span></div>
    <div class="strip-cta"><span>GET A QUOTE</span><span class="dl">DOWNLOAD</span></div>
  </div>
</header>

<main>
  <section>
    <div class="stats">
      <div class="stat" style="left:234px"><strong>25</strong>Years of experience</div>
      <div class="stat" style="left:424px"><strong>107</strong>Sites cleaned</div>
      <div class="stat" style="left:609px"><strong>31</strong>Safety awards</div>
    </div>
    <div class="talk">Let's talk about your next site cleanup</div>
  </section>

  <section class="who">
    <div class="photo" role="img" aria-label="Photo of a site supervisor in a yellow hard hat holding a clipboard, with crew and crane behind" style="left:670px;top:528px;width:530px;height:308px;background:linear-gradient(90deg,#ffffff 0%,#e7edf2 25%,#c8d3dc 60%,#9aa7b3 100%)"></div>
    <div class="who-head"><div class="eyebrow">About us</div><h2 class="title">Who we are</h2></div>
    <p class="who-text">We supply general labour, maintenance and cleaning crews to construction sites of every size. From first dig to final handover, we keep your site safe, clear and moving on schedule.</p>
    <p class="quote">We work with builders and site managers to keep every phase tidy and safe, so crews can do their best work and projects are handed over on time, every time.</p>
    <div class="photo" role="img" aria-label="Handwritten signature of the company director" style="left:220px;top:775px;width:90px;height:30px;background:linear-gradient(90deg,#ededed,#f8f8f8)"></div>
  </section>

  <section>
    <div class="band" role="img" aria-label="Green-tinted photo of a construction site" style="left:0;background:linear-gradient(180deg,#3a9a5d,#2b7d48)"><b>Trained site crews</b>Ready to start fast</div>
    <div class="band" role="img" aria-label="Yellow-tinted photo of site equipment" style="left:400px;background:linear-gradient(180deg,#f4c92a,#e2b50f)"><b>Safety assured</b>Full PPE on every job</div>
    <div class="band" role="img" aria-label="Dark-tinted photo of a building site" style="left:800px;background:linear-gradient(180deg,#4a4a46,#333330)"><b>Licensed &amp; insured</b>For your peace of mind</div>
  </section>

  <section class="services">
    <div class="ind-head"><div class="eyebrow">Services</div><h2 class="title">What we do on site</h2></div>
    <p class="ind-text">Labour, upkeep and cleaning for builders and contractors. One team to keep your site clear, safe and ready for each new phase.</p>
    <div class="tabs">
      <div class="tab active">Construction cleanup</div>
      <div class="tab">General labour</div>
      <div class="tab">Site maintenance</div>
      <div class="tab">Debris removal</div>
      <div class="tab">Final clean &amp; handover</div>
      <div class="tab">Pressure washing</div>
    </div>
    <div class="photo" role="img" aria-label="Photo of two workers in safety vests inspecting a cleaned site floor" style="left:484px;top:1135px;width:482px;height:221px;background:linear-gradient(135deg,#5d5d5a,#a7a59e 55%,#4d4c48)"></div>
    <div class="ind-caption">
      <h4>Construction Cleanup</h4>
      <p>We clear dust, offcuts and waste during each build phase, so your crews work safely and your site passes every inspection.</p>
    </div>
  </section>

  <section class="projects">
    <div class="eyebrow">Works</div>
    <h2 class="title">Recent projects</h2>
    <div class="filters"><span class="on">All</span><span>Cleanup</span><span>Labour</span><span>Upkeep</span><span>Debris</span><span>Handover</span></div>
    <div class="photo" role="img" aria-label="Photo of a worker in orange overalls and face shield cutting materials on site" style="left:234px;top:162px;width:357px;height:266px;background:linear-gradient(135deg,#d7c4a0,#e36a22 50%,#6e5a44)"></div>
    <div class="photo" role="img" aria-label="Photo of a cleared building site under a blue sky" style="left:609px;top:162px;width:169px;height:125px;background:linear-gradient(180deg,#2e5b9b,#9fb5cc 70%,#c8cfd6)"></div>
    <div class="photo" role="img" aria-label="Photo of a site tower silhouetted at sunset" style="left:796px;top:162px;width:170px;height:125px;background:linear-gradient(180deg,#3a2a22,#d98a3a 60%,#2b1f18)"></div>
    <div class="photo" role="img" aria-label="Photo of a worker with bright sparks on site" style="left:609px;top:303px;width:169px;height:125px;background:linear-gradient(135deg,#2a2e2b,#4c6a4f 60%,#1e221f)"></div>
    <div class="photo" role="img" aria-label="Photo of a crew in yellow hard hats on site" style="left:796px;top:303px;width:170px;height:125px;background:linear-gradient(180deg,#9aa4ab,#6d6a5e 60%,#3f3e38)"></div>
  </section>

  <section class="features">
    <div class="feat-head"><div class="eyebrow">Why choose us</div><h2 class="title">Awesome features</h2></div>

    <div class="feature" style="left:234px;top:2066px"><span class="ico"><svg width="16" height="16" viewBox="0 0 16 16"><circle cx="8" cy="8" r="6" fill="none" stroke="#34a35a" stroke-width="1.6"/></svg></span><div><h4>Modern equipment</h4><p>Industrial vacuums, sweepers and washers that leave every site clean, fast and with less dust.</p></div></div>
    <div class="feature" style="left:484px;top:2066px"><span class="ico"><svg width="16" height="16" viewBox="0 0 16 16"><path d="M8 2v12M3 8h10" stroke="#34a35a" stroke-width="1.6"/></svg></span><div><h4>Professional workers</h4><p>Skilled, vetted labourers who follow site rules and arrive ready with their own safety gear.</p></div></div>
    <div class="feature" style="left:234px;top:2144px"><span class="ico"><svg width="16" height="16" viewBox="0 0 16 16"><circle cx="8" cy="6" r="3" fill="none" stroke="#34a35a" stroke-width="1.6"/><path d="M3 14c1-3 9-3 10 0" fill="none" stroke="#34a35a" stroke-width="1.6"/></svg></span><div><h4>Flexible crews</h4><p>Scale up or down by the day, so you only pay for the hands you need on site.</p></div></div>
    <div class="feature" style="left:484px;top:2144px"><span class="ico"><svg width="16" height="16" viewBox="0 0 16 16"><path d="m3 3 10 10M13 3 3 13" stroke="#34a35a" stroke-width="1.8"/></svg></span><div><h4>Effective teamwork</h4><p>We work around your trades and schedule, keeping access routes clear and work areas safe.</p></div></div>
    <div class="feature" style="left:234px;top:2222px"><span class="ico"><svg width="16" height="16" viewBox="0 0 16 16"><rect x="3" y="3" width="10" height="10" fill="none" stroke="#34a35a" stroke-width="1.6"/></svg></span><div><h4>Maintenance</h4><p>Regular upkeep of fencing, walkways, welfare units and temporary works across the build.</p></div></div>
    <div class="feature" style="left:484px;top:2222px"><span class="ico"><svg width="16" height="16" viewBox="0 0 16 16"><rect x="2" y="4" width="12" height="9" fill="none" stroke="#34a35a" stroke-width="1.6"/><path d="M6 4V2h4v2" fill="none" stroke="#34a35a" stroke-width="1.6"/></svg></span><div><h4>A full service</h4><p>From rough clean to final sparkle clean, one team takes your site all the way to handover.</p></div></div>

    <aside class="testi">
      <span class="qmark"></span>
      <span class="avatar" role="img" aria-label="Portrait photo of the client"></span>
      <h4>Harlan Voss</h4>
      <span class="role">Site Manager, Building Contractor</span>
      <p>Their crew kept our site spotless through every phase. Debris was gone daily, walkways stayed clear and the final clean made handover easy. Reliable people who simply get the job done.</p>
    </aside>
    <svg class="abs" style="left:950px;top:2038px" width="8" height="30" viewBox="0 0 8 30"><path d="m2 1 4 4-4 4M6 21l-4 4 4 4" stroke="#666" fill="none" stroke-width="1.3"/></svg>
  </section>

  <section class="news">
    <div class="news-head"><div class="eyebrow">News</div><h2 class="title">Latest new</h2></div>
    <article class="card" style="left:234px">
      <div role="img" aria-label="Photo of a large building site seen across fields" style="height:124px;background:linear-gradient(180deg,#8fa0ad,#c9b48a 60%,#6e5d3e)"></div>
      <div class="meta"><b>Blog</b> — 06 Jul 2017</div>
      <h4>How a Daily Cleanup Routine Keeps Your Building Site Safer</h4>
      <p>Simple habits that cut trip hazards, keep inspectors happy and help every trade work faster on a clear, well kept site.</p>
    </article>
    <article class="card" style="left:479px">
      <div role="img" aria-label="Photo of new steel framing against a blue sky" style="height:124px;background:linear-gradient(180deg,#3f78b8,#9eb6cf 55%,#5b6670)"></div>
      <div class="meta"><b>Blog</b> — 12 Dec 2016</div>
      <h4>What to Expect From a Final Clean Before Project Handover</h4>
      <p>A step by step look at how our crews prepare finished buildings so owners walk into spaces that are spotless and ready.</p>
    </article>
    <article class="card" style="left:727px">
      <div role="img" aria-label="Photo of an old brick building under renovation" style="height:124px;background:linear-gradient(180deg,#7fa2c8,#9c5a3c 55%,#5a3426)"></div>
      <div class="meta"><b>Blog</b> — 08 Aug 2016</div>
      <h4>Smart ways to sort and recycle construction waste</h4>
      <p>How sorting timber, metal and rubble on site lowers skip costs and helps your project meet its green building goals.</p>
    </article>
  </section>

  <section class="partners" aria-label="Partners">
    <span class="partner"></span><span class="partner"></span><span class="partner round"></span><span class="partner round"></span><span class="partner"></span><span class="partner"></span>
  </section>

  <section class="contact-sec"></section>
  <div class="contact-head"><div class="eyebrow">Get in touch</div><h2 class="title">Contact us</h2></div>
  <div class="contact-brand"><i></i>Brixo Tidy Yard</div>
  <p class="contact-text">Our crews keep building sites clean, safe and on schedule. Tell us about your project and we will build a labour and cleaning plan that fits your site.</p>
  <div class="info" style="left:234px">
    <svg width="12" height="12" viewBox="0 0 12 12"><path d="M2 1h3l1 3-2 1a7 7 0 0 0 3 3l1-2 3 1v3c-6 0-10-4-10-9z" fill="none" stroke="#e25b45" stroke-width="1.1"/></svg>
    <div class="lbl">Have a question? Call us</div><div class="val">1800 - 555 204 19</div>
  </div>
  <div class="info" style="left:355px">
    <svg width="12" height="12" viewBox="0 0 12 12"><rect x="1" y="2.5" width="10" height="7" fill="none" stroke="#e25b45" stroke-width="1.1"/><path d="m1 3 5 4 5-4" fill="none" stroke="#e25b45" stroke-width="1.1"/></svg>
    <div class="lbl">Our contact form</div><div class="val">hello@brixotidy.com</div>
  </div>
  <div class="info" style="left:476px">
    <svg width="12" height="12" viewBox="0 0 12 12"><path d="M6 11S2 7 2 4.5a4 4 0 0 1 8 0C10 7 6 11 6 11z" fill="none" stroke="#e25b45" stroke-width="1.1"/><circle cx="6" cy="4.5" r="1.3" fill="#e25b45"/></svg>
    <div class="lbl">Find us at</div><div class="val">42 Quarry Lane, Leeds, United Kingdom</div>
  </div>
  <div class="abs" style="left:518px;top:3168px;display:flex;gap:9px"><i class="dot" style="width:7px;height:7px;background:#999"></i><i class="dot" style="width:7px;height:7px;background:#999"></i><i class="dot" style="width:7px;height:7px;background:#999"></i><i class="dot" style="width:7px;height:7px;background:#999"></i><i class="dot" style="width:7px;height:7px;background:#999"></i></div>

  <form class="form">
    <h3>Request quote</h3>
    <div class="row"><div class="field">First Name*</div><div class="field">Last Name*</div></div>
    <div class="row"><div class="field">Email*</div><div class="field">Your phone</div></div>
    <div class="row"><div class="field">Choose Service</div></div>
    <div class="row"><div class="field area">Message</div></div>
    <div class="btn">Get a quote</div>
  </form>
</main>

<footer class="footer">
  <span class="notch"></span>
  <span class="top">Go to top</span>
  <span class="copy">Copyright 2017 Brixo Tidy Yard - All rights reserved</span>
</footer>

</body>
</html>
```